Our 2023 Comprehensive Needs Assessment needs a cover. We take data and produce an indepth beautiful report for our clients. Attached is the color palette we are going with. Let me know if you need me to send any additional information. This cover will be printed as well as used digitally.

```html
<!DOCTYPE html>
<html lang="en">
<head>
<meta charset="utf-8">
<title>2023 Comprehensive Needs Assessment — Cover</title>
<link href="https://fonts.googleapis.com/css2?family=Bebas+Neue&display=swap" rel="stylesheet">
<style>
  :root {
    --green-top: #5fa952;
    --green-mid: #8cc63f;
    --yellow-bottom: #f2f700;
    --title-yellow: #f8f800;
    --title-pale: #d6f78e;
    --rule: #cdf08a;
    --art-dark: #3a7424;
    --art-mid: #4f8f33;
    --art-mint: #c9efc4;
    --art-pale: #e6f7d8;
  }
  * { margin: 0; padding: 0; box-sizing: border-box; }
  html, body { width: 800px; height: 1200px; overflow: hidden; background: #ffffff; }
  .cover {
    position: relative;
    width: 800px;
    height: 1200px;
    overflow: hidden;
    background: linear-gradient(215deg, var(--green-top) 0%, var(--green-mid) 45%, var(--yellow-bottom) 100%);
    font-family: "Bebas Neue", "Oswald", sans-serif;
  }
  .title-block {
    position: absolute;
    right: 51px;
    top: 34px;
    text-align: right;
    line-height: 1;
  }
  .year {
    display: block;
    font-size: 206px;
    color: var(--title-yellow);
    letter-spacing: 2px;
  }
  .rule {
    position: absolute;
    left: 0;
    top: 220px;
    width: 749px;
    height: 4px;
    background: var(--rule);
  }
  .heading {
    position: absolute;
    right: 51px;
    top: 244px;
    text-align: right;
    line-height: 0.9;
    font-weight: 400;
  }
  .heading span { display: block; }
  .heading .line-comprehensive { font-size: 96px; color: var(--title-yellow); }
  .heading .line-needs { font-size: 176px; color: var(--title-yellow); margin-top: -2px; }
  .heading .line-assessment { font-size: 118px; color: var(--title-pale); margin-top: 2px; }
  .illustration {
    position: absolute;
    left: 100px;
    top: 650px;
    width: 662px;
    height: 518px;
    border-radius: 28px;
    background:
      radial-gradient(circle at 61% 48%, var(--art-mid) 0%, var(--art-dark) 46%, rgba(58,116,36,0) 47%),
      linear-gradient(160deg, rgba(230,247,216,0.55) 0%, rgba(201,239,196,0.35) 55%, rgba(201,239,196,0) 100%);
  }
</style>
</head>
<body>
  <main class="cover">
    <div class="title-block">
      <span class="year">2023</span>
    </div>
    <div class="rule"></div>
    <h1 class="heading">
      <span class="line-comprehensive">Comprehensive</span>
      <span class="line-needs">Needs</span>
      <span class="line-assessment">Assessment</span>
    </h1>
    <div class="illustration" role="img" aria-label="Illustration of data dashboards with area, bar and pie charts, chat bubbles and a hand holding a magnifying glass, set on a dark green circle"></div>
  </main>
</body>
</html>
```